Tidewell Marketing company is looking for a web page design

Your projects should contain:

1. Header: Logo provided by us.
2. Top nav bar: offer, about us, experience, contact.
3. “Choose language” button.
4. Main section: panoramic picture (static, professional, modern).
5. Below section: 3 blocks (image+title+description), which represent our 3 main activities (titles):
• Market Research,
• Marketing Plans,
• Marketing Project.
6. ‘Contact us’ form – Message (text: “Write your message and give us details about your company and activities”), Email, SEND).
7. Page footer: (4 section: Contact, Social Media, Blog, Partners).
Updates

Hello!

I uploaded new file 'general_look', which is our idea how the page should generally look like.

BUT! it doesn't mean that your projects should look exactly like this project e.g.:
* titles Market Research, Marketing Plans, Marketing Project can be above these: Image 1,2,3.
* everything doesn't have to be in square and rectangle shape. You can try to manipulate with blocks and can add elipse elemnts or something similar.

We will appreciate your innovative ideas. Just wanted to give you general plan of the site and ilustrate all elements that we require.

Best Regards,
Benedek

IMPORTENT

Please remember that the main picture should be panoramic. Please do not close it in frame.

Target Market(s)

Small and middle sized companies, which would like to export their goods and services abroad and are interested in raising funds from Northgate Trade Council to expand their activities. These are rather industrial companies with low level of innovativeness. Our mission is to build image of the client’s company and increase awareness of their products to improve their competitiveness and innovativeness.

Industry/Entity Type

It Company

Requirements
Must have
• 1. Create designs of main page and subpage.
2. Subpage: Logo, Header, language button, place for article, navigation menu on the right side - below it “contact us” button , footer on the bottom. (In this section we are looking mainly for the design of the header and navigation menu).
3. The whole design should be a series of horizontal blocks.
4. Your projects should be associated with features such as: Reliability, Security, Professionalism, Openness, Uniqueness.
5. The design should be simple, fresh, readable, easy to use and should create a feeling of high quality services.
6. Possibility to change the panoramic picture (separate layer in a graphic file).
7. All pictures and blocks should be static, no movements.
8. Style of the page should be compliant with the logo design, font: Swiss.
9. Designs that we like: http://www.fernvale-studio.pl/, http://www.plumquarry.com/.
Should not have
• There shouldn’t be any distractions and not matching parts (whole design should be compact and easy to interpret and remember).

```html
<!DOCTYPE html>
<html lang="en">
<head>
<meta charset="utf-8">
<title>Tidewell Marketing</title>
<link rel="stylesheet" href="https://fonts.googleapis.com/css2?family=PT+Sans+Narrow:wght@400;700&family=Source+Sans+3:ital,wght@0,400;0,600;1,400&display=swap">
<style>
  :root {
    --navy: #003d6b;
    --brand: #1a4f7f;
    --nav: #4677a2;
    --block-top: #2f6694;
    --block-bottom: #5e8db8;
    --ink: #1c5588;
    --dark-btn: #1b1b1b;
    --pale: #cddbe6;
    --line: #cfd6dd;
    --white: #ffffff;
  }
  * { box-sizing: border-box; margin: 0; padding: 0; }
  html, body { width: 1200px; height: 1069px; overflow: hidden; background: var(--navy); }
  body { position: relative; font-family: "Source Sans 3", sans-serif; color: var(--ink); }
  .abs { position: absolute; }

  .page { position: absolute; left: 153px; top: 0; width: 894px; height: 817px;
    background: linear-gradient(#e9eef3 0, #ffffff 110px); }

  .logo { left: 171px; top: 26px; display: flex; align-items: center; gap: 8px; }
  .logo-mark { width: 54px; height: 54px; border-radius: 50%; background: var(--brand); }
  .logo-name { font-size: 36px; font-weight: 600; color: var(--brand); letter-spacing: -0.5px; }

  .language { left: 971px; top: 12px; font-size: 12px; color: #222; display: flex; align-items: center; gap: 6px; }
  .language svg { width: 8px; height: 5px; }

  .nav { left: 547px; top: 40px; display: flex; gap: 5px; }
  .nav a { width: 93px; height: 37px; background: var(--nav); color: var(--white);
    font-size: 12px; text-decoration: none; display: flex; align-items: center; justify-content: center; }

  .hero { left: 160px; top: 112px; width: 880px; height: 370px; background: var(--white);
    border: 1px solid var(--line); box-shadow: 0 6px 6px -3px rgba(0,0,0,.45); }
  .hero-title { left: 200px; top: 172px; font-family: "PT Sans Narrow", sans-serif; font-size: 34px; color: var(--brand); }
  .hero-text { left: 200px; top: 222px; width: 370px; font-size: 13px; line-height: 22px; }
  .btn-large { left: 199px; top: 305px; width: 91px; height: 28px; background: var(--dark-btn); color: var(--white);
    font-family: "PT Sans Narrow", sans-serif; font-size: 17px; display: flex; align-items: center; justify-content: center; }
  .pager { left: 197px; top: 440px; display: flex; gap: 4px; }
  .pager span { width: 18px; height: 19px; border: 1px solid var(--ink); font-size: 11px; display: flex; align-items: center; justify-content: center; }
  .hero-photo { left: 600px; top: 120px; width: 425px; height: 352px;
    background: radial-gradient(ellipse at 55% 55%, #9aa6b4 0, #c8d0da 45%, #ffffff 72%); }

  .activity { top: 473px; width: 277px; height: 158px; color: var(--white); padding: 10px 12px 0 13px;
    background: linear-gradient(160deg, var(--block-top), var(--block-bottom));
    box-shadow: 0 12px 10px -8px rgba(0,0,0,.55); }
  .activity h2 { font-weight: 400; font-size: 21px; line-height: 24px; padding-bottom: 4px; border-bottom: 1px solid rgba(255,255,255,.35); }
  .activity p { font-size: 12px; line-height: 18.5px; padding: 9px 0 0 2px; }
  .btn-small { background: var(--dark-btn); color: var(--white); font-size: 12px; height: 20px;
    display: flex; align-items: center; justify-content: center; }
  .activity .btn-small { position: absolute; right: 9px; bottom: 7px; width: 55px; }

  .section-title { font-size: 21px; font-weight: 400; color: var(--brand); }
  .offer-image { left: 219px; top: 678px; width: 169px; height: 139px;
    background: radial-gradient(circle at 45% 40%, #e02c2c 0, #e02c2c 35%, #f3c9ab 36%, #ffffff 70%); }
  .offer-text { left: 421px; top: 684px; width: 320px; font-size: 13px; line-height: 22px; }
  .field { background: var(--white); border: 1px solid var(--line); font-size: 12px; color: #888; padding-left: 8px; display: flex; align-items: center; }

  .footer-title { font-size: 21px; color: var(--white); font-weight: 400; }
  .thumb { width: 57px; height: 49px; border-radius: 8px; background: var(--pale); }
  .blog-text { font-size: 11.5px; line-height: 17px; font-style: italic; color: var(--white); width: 140px; }
  .contact-field { background: var(--white); border: 1px solid #c7d3de; }
  .send { left: 678px; top: 1012px; width: 80px; height: 25px; background: var(--dark-btn); color: var(--white);
    font-size: 19px; display: flex; align-items: center; justify-content: center; }
  .social { left: 859px; top: 894px; display: flex; gap: 6px; }
  .social span { width: 23px; height: 23px; border-radius: 3px; background: #4f88bf; }
  .social-links { left: 856px; top: 938px; font-size: 12px; color: var(--white); word-spacing: 2px; }
  .copyright { left: 855px; top: 969px; font-size: 12px; color: var(--white); }
</style>
</head>
<body>
  <div class="page"></div>

  <div class="abs logo"><span class="logo-mark"></span><span class="logo-name">Tidewell Marketing</span></div>
  <div class="abs language">Language
    <svg viewBox="0 0 8 5"><path d="M0 0h8L4 5z" fill="#222"/></svg></div>

  <nav class="abs nav">
    <a href="#">Home</a><a href="#">Offers</a><a href="#">About us</a><a href="#">Experience</a><a href="#">Contact Us</a>
  </nav>

  <section class="abs hero"></section>
  <h1 class="abs hero-title" style="font-weight:400">Heading</h1>
  <p class="abs hero-text">Lorem Ipsum is simply dummy text of the printing and typesetting industry. Lorem Ipsum has been the industry's standard dummy text ever since the 1500s,</p>
  <div class="abs btn-large">Get More</div>
  <div class="abs pager"><span>1</span><span>2</span><span>3</span><span>4</span><span>5</span></div>
  <div class="abs hero-photo" role="img" aria-label="Group of cheering business people in suits"></div>

  <article class="abs activity" style="left:176px">
    <h2>Market Research</h2>
    <p>Lorem Ipsum is simply dummy text of the printing and typesetting industry. Lorem Ipsum has been the industry's standard dummy text ever since the 1500s,</p>
    <div class="btn-small">more &gt;&gt;</div>
  </article>
  <article class="abs activity" style="left:461px">
    <h2>Marketing Plans</h2>
    <p>Lorem Ipsum is simply dummy text of the printing and typesetting industry. Lorem Ipsum has been the industry's standard dummy text ever since the 1500s,</p>
    <div class="btn-small">more &gt;&gt;</div>
  </article>
  <article class="abs activity" style="left:746px">
    <h2>Marketing Project</h2>
    <p>Lorem Ipsum is simply dummy text of the printing and typesetting industry. Lorem Ipsum has been the industry's standard dummy text ever since the 1500s,</p>
    <div class="btn-small">more &gt;&gt;</div>
  </article>

  <h2 class="abs section-title" style="left:177px;top:650px">offers</h2>
  <div class="abs offer-image" role="img" aria-label="Hand holding a red special offer star badge"></div>
  <p class="abs offer-text">Lorem Ipsum is simply dummy text of the printing and typesetting industry. Lorem Ipsum has been the industry's standard dummy text ever since the 1500s,</p>
  <div class="abs btn-small" style="left:420px;top:772px;width:55px">more &gt;&gt;</div>

  <h2 class="abs section-title" style="left:766px;top:650px">subscribe</h2>
  <div class="abs field" style="left:768px;top:688px;width:253px;height:25px">Enter email id</div>
  <div class="abs field" style="left:768px;top:724px;width:253px;height:25px">Message</div>
  <div class="abs btn-small" style="left:770px;top:772px;width:55px">subscribe</div>

  <h2 class="abs footer-title" style="left:166px;top:836px">Blog</h2>
  <div class="abs thumb" style="left:163px;top:883px"></div>
  <p class="abs blog-text" style="left:229px;top:883px">Lorem ipsum dolor sit amet, consectetuer adipiscing elit. Nam cursus.</p>
  <div class="abs thumb" style="left:163px;top:949px"></div>
  <p class="abs blog-text" style="left:229px;top:947px">Lorem ipsum dolor sit amet, consectetuer adipiscing elit. Nam cursus.</p>

  <h2 class="abs footer-title" style="left:393px;top:839px">Partners</h2>
  <div class="abs thumb" style="left:388px;top:885px"></div>
  <div class="abs thumb" style="left:460px;top:885px"></div>
  <div class="abs thumb" style="left:533px;top:885px"></div>
  <div class="abs thumb" style="left:388px;top:947px"></div>
  <div class="abs thumb" style="left:460px;top:947px"></div>
  <div class="abs thumb" style="left:533px;top:947px"></div>

  <h2 class="abs footer-title" style="left:618px;top:846px">Contact Us</h2>
  <div class="abs contact-field" style="left:620px;top:891px;width:200px;height:25px"></div>
  <div class="abs contact-field" style="left:620px;top:924px;width:200px;height:25px"></div>
  <div class="abs contact-field" style="left:620px;top:957px;width:200px;height:44px"></div>
  <div class="abs send">Send</div>

  <h2 class="abs footer-title" style="left:858px;top:849px">Follow Us on</h2>
  <div class="abs social"><span></span><span></span><span></span><span></span></div>
  <p class="abs social-links">Friendlane | Linkpath | Chirper | RSS</p>
  <p class="abs copyright">Copyrights @ 2012 All Rights Reserved</p>
</body>
</html>
```